Face cream packaging | Cosmetic start-up

This project is about creating design proposals for two different types of packaging. Once to a cream jar made of glass and once to a jar made of plastic.
Three different designs must be created for each type of jar. Later, the different packaging will be used as customization options in an online store for cosmetics.

- The packaging variant made of glass should have color gradients. Three different shades are to be chosen. (Preferably with the primary colors red, blue and green). Note: The designer can create other proposals at will if he has better ideas. The logo must be included in some form. (Link to manufacturer description: https://catalogue.valdorpackaging.com/en/portals/valdorpackaging/assets/12667188/lou-50-ml/)

- With the plastic type of packaging, the designer has a lot of freedom to design. The only requirement is that the design must be artistic. It doesn't matter whether abstract patterns, geometric figures, mandalas or just a basic color is chosen. The main thing is that the packaging inspires. The logo must be included in some form. (Link to manufacturer description: https://catalogue.valdorpackaging.com/en/portals/valdorpackaging/assets/12667181/edda-50-ml/)

Thank you in advance for your work and best regards
Olaf

Target Market(s)

Young people with an affinity for social media and the web. Focus is on the female clientele.

Industry/Entity Type

Cosmetics

Font styles to use
Script

Colors
eea4c8
f59195
85cae6
cadf82

Requirements
Must have
• The logo must be included in some form. (PNG-File attached)
Nice to have
• Other types of packaging (can shape, packaging material)

```html
<!DOCTYPE html>
<html lang="en">
<head>
<meta charset="utf-8">
<title>Face Cream Labels</title>
<link href="https://fonts.googleapis.com/css2?family=Josefin+Sans:wght@300;400;600&display=swap" rel="stylesheet">
<style>
  :root {
    --canvas-bg: #ffffff;
    --ink: #4a4a4a;
    --rule: #6a6a6a;
    --blue-light: #c2e8f8;
    --blue-mid: #9fd4ee;
    --blue-deep: #6cb3d6;
    --green-light: #eaf7b8;
    --green-mid: #d8ec9e;
    --green-deep: #bcd477;
    --pink-light: #ffc4c6;
    --pink-mid: #f7a6a9;
    --pink-deep: #ec8589;
  }
  html, body {
    margin: 0;
    padding: 0;
    overflow: hidden;
    background: var(--canvas-bg);
  }
  .canvas {
    position: relative;
    width: 1200px;
    height: 800px;
    background: var(--canvas-bg);
    overflow: hidden;
    font-family: "Josefin Sans", sans-serif;
    color: var(--ink);
  }
  .label {
    position: absolute;
    width: 332px;
    height: 140px;
    box-sizing: border-box;
  }
  .label--blue {
    left: 168px; top: 300px;
    background:
      linear-gradient(90deg, rgba(0,0,0,0.08) 0%, rgba(255,255,255,0) 22%, rgba(255,255,255,0) 78%, rgba(0,0,0,0.08) 100%),
      linear-gradient(180deg, var(--blue-light) 0%, var(--blue-mid) 55%, var(--blue-deep) 100%);
  }
  .label--green {
    left: 712px; top: 300px;
    background:
      linear-gradient(90deg, rgba(0,0,0,0.06) 0%, rgba(255,255,255,0) 22%, rgba(255,255,255,0) 78%, rgba(0,0,0,0.06) 100%),
      linear-gradient(180deg, var(--green-light) 0%, var(--green-mid) 55%, var(--green-deep) 100%);
  }
  .label--pink {
    left: 452px; top: 486px;
    background:
      linear-gradient(90deg, rgba(0,0,0,0.06) 0%, rgba(255,255,255,0) 22%, rgba(255,255,255,0) 78%, rgba(0,0,0,0.06) 100%),
      linear-gradient(180deg, var(--pink-light) 0%, var(--pink-mid) 55%, var(--pink-deep) 100%);
  }
  .brand {
    position: absolute;
    left: 120px;
    top: 34px;
    font-size: 15px;
    font-weight: 300;
    letter-spacing: 1px;
    color: var(--ink);
    white-space: nowrap;
    padding-bottom: 3px;
    border-bottom: 1px solid var(--rule);
  }
  .product-name {
    position: absolute;
    left: 0; right: 0;
    top: 98px;
    text-align: center;
    font-size: 9.5px;
    font-weight: 600;
    letter-spacing: 5px;
    padding-left: 5px;
  }
  .volume {
    position: absolute;
    left: 0; right: 0;
    top: 117px;
    text-align: center;
    font-size: 9px;
    font-weight: 600;
  }
</style>
</head>
<body>
  <main class="canvas">
    <section class="label label--blue">
      <div class="brand">Mira Lune</div>
      <div class="product-name">FACE CREAM</div>
      <div class="volume">50ml</div>
    </section>
    <section class="label label--green">
      <div class="brand">Mira Lune</div>
      <div class="product-name">FACE CREAM</div>
      <div class="volume">50ml</div>
    </section>
    <section class="label label--pink">
      <div class="brand">Mira Lune</div>
      <div class="product-name">FACE CREAM</div>
      <div class="volume">50ml</div>
    </section>
  </main>
</body>
</html>
```